Cutting Edge Cloud Hosting Provider needs business card design

We are a new Cloud Hosting Provider called Velkaro Hosting. (Velkaro means cloudy in Spanish.) We provide clients with virtual resources and not virtual machines directly. Our clients purchase the resources that they will use (RAM,CPU, Hard drive space) then use those resources in as many virtual machines as they like.

We are looking for a business card design that is cutting edge and hip.
Updates

The name of the company is "Velkaro Hosting". Please include the "Hosting" part of our name in the design.

Thanks

Target Market(s)

21-35 developers and I.T. Staff

Industry/Entity Type

Business

Requirements
Must have
• Rounded corners, Must Incorporate our logo, individual's name must be prominent

```html
<!DOCTYPE html>
<html lang="en">
<head>
<meta charset="utf-8">
<title>Velkaro Hosting – Business Card</title>
<link href="https://fonts.googleapis.com/css2?family=Saira:wght@400;500;600&display=swap" rel="stylesheet">
<style>
  :root {
    --backdrop: #3b3b3d;
    --green: #17b26b;
    --green-deep: #0fa862;
    --green-light: #4cc683;
    --lime: #d3ec9c;
    --white: #ffffff;
    --strip: rgba(255, 255, 255, 0.16);
  }
  * { margin: 0; padding: 0; box-sizing: border-box; }
  html, body {
    width: 1200px; height: 534px; overflow: hidden;
    background: var(--backdrop);
    font-family: "Saira", sans-serif;
  }
  .canvas { position: relative; width: 1200px; height: 534px; }
  .card {
    position: absolute; top: 119px;
    width: 517px; height: 293px;
    border-radius: 18px; overflow: hidden;
  }

  /* Front */
  .card--front {
    left: 62px;
    background: linear-gradient(135deg, var(--lime) 0%, var(--green-light) 28%, var(--green) 60%, var(--green-deep) 100%);
  }
  .front-sheen {
    position: absolute; inset: 0;
    background: radial-gradient(ellipse 60% 70% at 85% 10%, rgba(255,255,255,0.18), transparent 70%);
  }
  .front-name {
    position: absolute; left: 0; right: 0; top: 122px;
    text-align: center; color: var(--white);
    font-size: 46px; font-weight: 600; line-height: 1;
  }
  .front-strip {
    position: absolute; left: 0; right: 0; top: 265px; height: 28px;
    background: var(--strip);
  }
  .front-web {
    position: absolute; left: 0; right: 0; top: 270px;
    text-align: center; color: var(--white);
    font-size: 13px; font-weight: 500; letter-spacing: 4.5px;
  }

  /* Back */
  .card--back { left: 622px; background: var(--white); }
  .back-top-pattern {
    position: absolute; right: 0; top: 0; width: 240px; height: 125px;
    background: radial-gradient(ellipse 80% 90% at 100% 30%, rgba(23,178,107,0.10), transparent 75%);
  }
  .back-logo-name {
    position: absolute; left: 26px; top: 44px;
    color: var(--green); font-size: 30px; font-weight: 600; line-height: 1;
  }
  .back-band {
    position: absolute; left: 0; right: 0; top: 125px; bottom: 0;
    background: linear-gradient(180deg, var(--green) 0%, var(--green-light) 60%, var(--green) 100%);
  }
  .back-strip {
    position: absolute; left: 0; right: 0; top: 265px; height: 14px;
    background: var(--strip);
  }
  .person { position: absolute; left: 51px; top: 170px; color: var(--white); }
  .person-name { font-size: 20px; font-weight: 500; line-height: 1; letter-spacing: 0.5px; }
  .person-title { font-size: 11.5px; font-weight: 600; line-height: 1.2; margin-top: 2px; }
  .person-web {
    position: absolute; left: 51px; top: 229px;
    color: var(--white); font-size: 13px; font-weight: 500; letter-spacing: 0.5px;
  }
  .divider {
    position: absolute; left: 293px; top: 177px; width: 1px; height: 68px;
    background: rgba(255,255,255,0.7);
  }
  .contact-list {
    position: absolute; left: 306px; top: 177px; list-style: none;
    color: var(--white); font-size: 13px; font-weight: 500; letter-spacing: 0.5px;
  }
  .contact-list li { line-height: 26px; }
</style>
</head>
<body>
<div class="canvas">

  <section class="card card--front" aria-label="Business card front">
    <div class="front-sheen" role="img" aria-label="Soft flowing line pattern over green gradient"></div>
    <div class="front-name">Velkaro Hosting</div>
    <div class="front-strip"></div>
    <div class="front-web">WWW.VELKARO.COM</div>
  </section>

  <section class="card card--back" aria-label="Business card back">
    <div class="back-top-pattern" role="img" aria-label="Faint curved line pattern"></div>
    <div class="back-logo-name">Velkaro Hosting</div>
    <div class="back-band"></div>
    <div class="back-strip"></div>
    <div class="person">
      <div class="person-name">DARIO LUNEZ</div>
      <div class="person-title">VICE-PRESIDENT</div>
    </div>
    <div class="person-web">W: WWW.VELKARO.COM</div>
    <div class="divider"></div>
    <ul class="contact-list">
      <li>P. 555.214.3870</li>
      <li>C. 555.608.2291</li>
      <li>E: DARIO@VELKARO.COM</li>
    </ul>
  </section>

</div>
</body>
</html>
```